Super elegant, crisp & clean Business card design required

We recently upgraded our branding - which is on our website - tavorelstudio.com

I would like a simple, yet elegant, clean business card design please.

The font of my logo is Cinzel - and because of the natural colour - it's best to have this on a black background.

I would like to have the back of the business card - with simply my logo.

PLEASE DO NOT SUBMIT A COMPLICATED / UNCLEAN DESIGN

Industry/Entity Type

Business

Contact Information for Business Card

Dalvik Ostrander Photography

Font styles to use
Other font styles liked:
• Cinzel

Requirements
Must have
• A backpage with nothing but my logo
• Simple design - stands out
Should not have
• Colour that dont align with my logo
• Over complicated '/ non symmetrical design

```html
<!DOCTYPE html>
<html lang="en">
<head>
<meta charset="utf-8">
<title>Dalvik Ostrander Photography — Business Cards</title>
<link href="https://fonts.googleapis.com/css2?family=Cinzel:wght@400;500&family=Montserrat:wght@300;400&display=swap" rel="stylesheet">
<style>
  :root {
    --backdrop: #2a2b2d;
    --card: #17191b;
    --gold: #a88f6b;
    --gold-soft: #8f7a5c;
  }
  * { margin: 0; padding: 0; box-sizing: border-box; }
  html, body { width: 1200px; height: 1189px; overflow: hidden; }
  body {
    background: var(--backdrop);
    position: relative;
    font-family: 'Montserrat', sans-serif;
    color: var(--gold);
  }
  .card {
    position: absolute;
    left: 170px;
    width: 860px;
    height: 491px;
    background: var(--card);
    border-radius: 26px;
    box-shadow: 0 18px 40px rgba(0,0,0,0.45);
  }
  .card--back { top: 70px; }
  .card--front { top: 628px; }

  .wordmark { text-align: center; font-family: 'Cinzel', serif; color: var(--gold); }
  .wordmark__mark {
    display: block; width: 18px; height: 18px; margin: 0 auto 22px;
    border: 1.5px solid var(--gold); border-radius: 50%;
  }
  .wordmark__name { font-size: 34px; font-weight: 400; letter-spacing: 1px; white-space: nowrap; }
  .wordmark__tag { font-size: 15px; letter-spacing: 12px; margin-top: 4px; padding-left: 12px; }

  .card--back .wordmark {
    position: absolute; left: 0; right: 0; top: 50%; transform: translateY(-50%);
  }

  .card--front .wordmark {
    position: absolute; left: 30px; width: 400px; top: 50%; transform: translateY(-50%);
  }
  .card--front .wordmark__name { font-size: 28px; }
  .card--front .wordmark__tag { font-size: 13px; letter-spacing: 10px; }

  .divider {
    position: absolute; left: 452px; top: 70px; bottom: 70px;
    width: 1.5px; background: var(--gold-soft);
  }

  .contact { position: absolute; left: 490px; top: 80px; right: 30px; }
  .contact__name { font-family: 'Cinzel', serif; font-size: 30px; letter-spacing: 1px; line-height: 1; }
  .contact__role { font-size: 17px; font-weight: 300; margin-top: 4px; }
  .contact__list { list-style: none; margin-top: 88px; }
  .contact__item {
    display: flex; align-items: center; gap: 12px;
    font-size: 19px; font-weight: 300; line-height: 1.45; white-space: nowrap;
  }
  .contact__item svg { width: 15px; height: 15px; flex: none; fill: var(--gold); }
</style>
</head>
<body>

<section class="card card--back" aria-label="Business card back">
  <div class="wordmark">
    <span class="wordmark__mark"></span>
    <div class="wordmark__name">Dalvik Ostrander</div>
    <div class="wordmark__tag">PHOTOGRAPHY</div>
  </div>
</section>

<section class="card card--front" aria-label="Business card front">
  <div class="wordmark">
    <span class="wordmark__mark"></span>
    <div class="wordmark__name">Dalvik Ostrander</div>
    <div class="wordmark__tag">PHOTOGRAPHY</div>
  </div>

  <div class="divider"></div>

  <div class="contact">
    <div class="contact__name">ROWAN PELL</div>
    <div class="contact__role">Chief Executive Officer</div>
    <ul class="contact__list">
      <li class="contact__item">
        <svg viewBox="0 0 16 16" aria-hidden="true"><path d="M3.6 1.2l2.3 2.6-1.3 1.8c.8 1.9 2.2 3.4 4.1 4.3l1.8-1.3 2.6 2.3-1.2 2.4C6.4 13 2.9 9.4 1.2 3.9z"/></svg>
        44 7700 900321
      </li>
      <li class="contact__item">
        <svg viewBox="0 0 16 16" aria-hidden="true"><path d="M1 3h14v10H1z M2.2 4.2v.4L8 8.6l5.8-4v-.4z" fill-rule="evenodd"/></svg>
        do.photography@tavorelmail.com
      </li>
      <li class="contact__item">
        <svg viewBox="0 0 16 16" aria-hidden="true"><path d="M8 1a7 7 0 1 0 0 14A7 7 0 0 0 8 1zm0 1.3c.8.8 1.4 2.2 1.6 3.7H6.4C6.6 4.5 7.2 3.1 8 2.3zM6.3 7.3h3.4v1.4H6.3zM6.4 10h3.2c-.2 1.5-.8 2.9-1.6 3.7-.8-.8-1.4-2.2-1.6-3.7zM2.4 7.3h2.6v1.4H2.4zm8.6 0h2.6v1.4H11z"/></svg>
        www.tavorelstudio.com
      </li>
    </ul>
  </div>
</section>

</body>
</html>
```